FROSTVITAL

We need 2 different business card designs for our new company FrostVital based in Los Angeles,California. Both cards will have front and back designs, There is 2 different cards we need designed. I submitted payment of $90. Please let me know if we need to submit another payment..
We liked this designs and I have attached our fav styles named card 1 and card 2.
Brief info about our company, our main service is the Cryotherpahy Chamber, the many benefits of Cryotherapy include overall wellness, weight loss, athletic recovery and beauty & anti-aging. Explanation on benefits is in pic attached. The final design should communicate wellness.
Wording and colors we want on card:
DESIGN card 1-
Colors: white and blues feel free to experiment (the current colors of the card are pretty good with the look we want. We just want to Logo to flow with the color of the card.
FRONT OF CARD:
FrstVital logo ( see attached logos in all formats)
Cryotherapy services
Mark Penterova Owner/Partner
Cell phone icon- 818-555-0193
Office Phone Icon- 805-555-0148
email icon- Mark@frost-vital.example
www.frost-vital.example
————————
2918 W MAPLEFIELD AVE.
WEST LAKE VILLAGE, CA 91362
BACK OF CARD ( you can play with different colors here as well.) Same concept with the blues whites and grey
Health & Wellness
*
Weight Loss
*
Athletic Recovery
*
Beauty & Anti-Aging
-------------------------------------------------
DESIGN Card 2-
On your current card there is water drops. We are trying to get the concept of a cold theme. Maybe snow flakes instead of water drops. See our attached picture with the machine and Ice/snow theme
FRONT OF CARD:
Cryotherapy services
email icon- Info@frost-vital.example
www.frost-vital.example
————————
WESTLAKE VILLAGE, CA 91362
BACK OF CARD option 1:
20% off your 1st Whole Body Cryo Package
or
50% off First Whole Body Cryo Session
Discover FrostVital!
Just 3 Minutes For Total Body CryoTherapy
* first time Guests only. Certain Restrictions Apply (please put this in very small writing on the bottom of the card )
Back Of Card Option 2 ( I need the same exact thing on the front of the card, same color schemes. The only changes we need is to have on the Back.
1 Free Whole Body Cryo Session
Discover FrostVital!
Certain Restrictions Apply (please put this in very small writing on the bottom of the card )

```html
<!DOCTYPE html>
<html lang="en">
<head>
<meta charset="utf-8">
<title>FrostVital Business Cards</title>
<link href="https://fonts.googleapis.com/css2?family=Open+Sans:ital,wght@0,400;0,600;0,700;1,400&display=swap" rel="stylesheet">
<style>
  :root {
    --stage: #071c25;
    --card-white: #ffffff;
    --wave-light: #8fcdea;
    --wave-mid: #3fa6d8;
    --wave-main: #0b8fcc;
    --name-blue: #2b6cb0;
    --title-blue: #8fb2d3;
    --brand-blue: #3bb5e3;
    --text-white: #ffffff;
    --faint-brand: #34393b;
  }
  * { margin: 0; padding: 0; box-sizing: border-box; }
  html, body {
    width: 1200px; height: 1000px; overflow: hidden;
    background: var(--stage);
    font-family: "Open Sans", Arial, sans-serif;
  }
  .stage { position: relative; width: 1200px; height: 1000px; }
  .card {
    position: absolute; width: 594px; height: 355px;
    background: var(--card-white); overflow: hidden;
  }
  .card--a { left: 6px; top: 5px; }
  .card--b { left: 602px; top: 5px; }
  .card--c { left: 6px; top: 365px; }
  .card--d { left: 602px; top: 365px; }
  .card__wave { position: absolute; left: 0; top: 0; width: 594px; height: 355px; }
  .brand {
    position: absolute; left: 58px; top: 102px;
    display: flex; align-items: center; gap: 12px;
  }
  .brand__dot {
    width: 30px; height: 30px; border-radius: 50%;
    background: var(--brand-blue);
  }
  .brand__name {
    font-weight: 600; font-size: 38px; color: var(--brand-blue);
    letter-spacing: -0.5px;
  }
  .person {
    position: absolute; right: 47px; top: 50px; text-align: right;
  }
  .person__name {
    font-weight: 700; font-size: 25px; color: var(--name-blue); line-height: 1.2;
  }
  .person__title {
    font-style: italic; font-size: 13px; color: var(--title-blue); padding-right: 4px;
  }
  .contact {
    position: absolute; left: 44px; top: 245px; list-style: none;
    color: var(--text-white); font-size: 13px;
  }
  .contact li { display: flex; align-items: center; gap: 7px; height: 22.5px; }
  .contact svg { width: 11px; height: 12px; flex: none; }
  .company {
    position: absolute; right: 49px; top: 229px; text-align: right;
    color: var(--text-white); font-size: 13px; line-height: 21.3px;
  }
  .backdrop-brand {
    position: absolute; left: 440px; top: 812px;
    font-weight: 700; font-size: 112px; color: var(--faint-brand);
    letter-spacing: 1px;
  }
</style>
</head>
<body>
<main class="stage">

  <svg width="0" height="0" style="position:absolute">
    <defs>
      <symbol id="wave" viewBox="0 0 594 355">
        <path d="M0,178 C100,226 200,240 320,212 C430,184 510,160 594,164 L594,355 L0,355 Z" fill="var(--wave-light)"/>
        <path d="M0,198 C100,236 220,240 340,210 C440,186 520,170 594,174 L594,355 L0,355 Z" fill="var(--wave-mid)"/>
        <path d="M0,228 C130,244 250,226 360,202 C450,182 530,178 594,184 L594,355 L0,355 Z" fill="var(--wave-main)"/>
      </symbol>
      <symbol id="icon-mobile" viewBox="0 0 11 12">
        <rect x="2.5" y="0.5" width="6" height="11" rx="1" fill="none" stroke="#fff" stroke-width="1"/>
        <line x1="4.5" y1="10" x2="6.5" y2="10" stroke="#fff" stroke-width="1"/>
      </symbol>
      <symbol id="icon-phone" viewBox="0 0 11 12">
        <path d="M2.5,0.8 L4.3,3.3 L3.3,4.6 C4,6.5 5,7.8 6.8,8.8 L8,7.8 L10.3,9.5 L9,11.3 C5,11 1.2,6.5 1,2.2 Z" fill="#fff"/>
      </symbol>
      <symbol id="icon-mail" viewBox="0 0 11 12">
        <rect x="0.5" y="3" width="10" height="7" fill="none" stroke="#fff" stroke-width="1"/>
        <polyline points="0.5,3 5.5,7 10.5,3" fill="none" stroke="#fff" stroke-width="1"/>
      </symbol>
    </defs>
  </svg>

  <div class="backdrop-brand">FrostVital</div>

  <article class="card card--a">
    <svg class="card__wave"><use href="#wave"/></svg>
    <div class="brand"><span class="brand__dot"></span><span class="brand__name">FrostVital</span></div>
    <div class="person"><div class="person__name">Mark Penterova</div><div class="person__title">Owner</div></div>
    <ul class="contact">
      <li><svg><use href="#icon-mobile"/></svg>818.555.0193</li>
      <li><svg><use href="#icon-phone"/></svg>805.555.0148</li>
      <li><svg><use href="#icon-mail"/></svg>mark@frost-vital.example</li>
    </ul>
    <div class="company">Cryotherapy Services<br>www.frost-vital.example<br>2918 W Maplefield Ave.<br>Westlake Village, CA 91362</div>
  </article>

  <article class="card card--b">
    <svg class="card__wave"><use href="#wave"/></svg>
    <div class="brand"><span class="brand__dot"></span><span class="brand__name">FrostVital</span></div>
    <div class="person"><div class="person__name">Lance Whitmore</div><div class="person__title">Owner</div></div>
    <ul class="contact">
      <li><svg><use href="#icon-mobile"/></svg>818.555.0127</li>
      <li><svg><use href="#icon-phone"/></svg>805.555.0148</li>
      <li><svg><use href="#icon-mail"/></svg>lance@frost-vital.example</li>
    </ul>
    <div class="company">Cryotherapy Services<br>www.frost-vital.example<br>2918 W Maplefield Ave.<br>Westlake Village, CA 91362</div>
  </article>

  <article class="card card--c">
    <svg class="card__wave"><use href="#wave"/></svg>
    <div class="brand"><span class="brand__dot"></span><span class="brand__name">FrostVital</span></div>
    <div class="person"><div class="person__name">Glen Harlow</div><div class="person__title">General Manager</div></div>
    <ul class="contact">
      <li><svg><use href="#icon-mobile"/></svg>661.555.0162</li>
      <li><svg><use href="#icon-phone"/></svg>805.555.0148</li>
      <li><svg><use href="#icon-mail"/></svg>glen@frost-vital.example</li>
    </ul>
    <div class="company">Cryotherapy Services<br>www.frost-vital.example<br>2918 W Maplefield Ave.<br>Westlake Village, CA 91362</div>
  </article>

  <article class="card card--d">
    <svg class="card__wave"><use href="#wave"/></svg>
    <div class="brand"><span class="brand__dot"></span><span class="brand__name">FrostVital</span></div>
    <div class="person"><div class="person__name">Victor Almonte</div><div class="person__title">Owner</div></div>
    <ul class="contact">
      <li><svg><use href="#icon-mobile"/></svg>818.555.0185</li>
      <li><svg><use href="#icon-phone"/></svg>805.555.0148</li>
      <li><svg><use href="#icon-mail"/></svg>victor@frost-vital.example</li>
    </ul>
    <div class="company">Cryotherapy Services<br>www.frost-vital.example<br>2918 W Maplefield Ave.<br>Westlake Village, CA 91362</div>
  </article>

</main>
</body>
</html>
```